I need to redesign my landing page into a high converting landing page adding 3 new elements

I need to redesign my landing page using all the same content, images etc. on the current page https://www.brightlanepromoworks.biz/travel_agency but also adding three new elements to the new redesign.

Please be sure to use my current header and footer from my current website since I will just plug the new design into it...

The Three New Elements Are Below (add these 3 new elements in addition to the current content)

1. Add a video element with this content:
Watch Below To See How Your Industry Uses Our Incentives To Skyrocket Their Sales!

2. Add the element of the 6 types of incentives they can offer.
You can use the same content and images that we use in this module on the homepage at www.brightlanepromoworks.biz ATTACHED IMAGE BUT YOU CAN FIND THE ORIGINAL IMAGES ON HOMEPAGE

3. Add 1 more call to action to give website visitors two choices:
A. Sign Up For 14 Days Risk Free
OR
B. Book A Live Call

Target Market(s)

Travel agents and travel advisors

Industry/Entity Type

marketing

Requirements
Must have
• HIGH CONVERTING LANDING PAGE
Nice to have
• short and to the point...no fluff

```html
<!DOCTYPE html>
<html lang="en">
<head>
<meta charset="utf-8">
<title>BrightLane Promo Works – Travel Agency Incentives</title>
<link href="https://fonts.googleapis.com/css2?family=Poppins:wght@400;500;600;700&display=swap" rel="stylesheet">
<style>
:root{
  --blue:#1a72c2;
  --blue-deep:#1565b6;
  --blue-text:#1b6cbf;
  --orange:#f6921e;
  --grey-btn:#585858;
  --grey-bg:#f3f3f3;
  --text:#2a2a2a;
  --muted:#8a8a8a;
  --white:#ffffff;
}
*{box-sizing:border-box;margin:0;padding:0}
html,body{width:1200px;height:4110px;overflow:hidden}
body{position:relative;font-family:"Poppins",sans-serif;color:var(--text);background:var(--white)}
.abs{position:absolute}
.btn{position:absolute;display:flex;align-items:center;justify-content:center;border-radius:20px;color:var(--white);font-size:11.5px;font-weight:600;height:34px}
.btn-orange{background:var(--orange)}
.btn-grey{background:var(--grey-btn)}
.photo{position:absolute}

/* header */
.site-header{top:0;left:0;width:1200px;height:56px;background:var(--white)}
.brand{position:absolute;left:156px;top:16px;display:flex;align-items:center;gap:8px;color:var(--blue-text);font-weight:600;font-size:16px}
.brand-mark{width:20px;height:20px;background:var(--blue-text)}
.account-links{position:absolute;right:155px;top:20px;display:flex;gap:16px;font-size:11px;color:var(--blue-text)}
.account-links span{display:flex;align-items:center;gap:4px}

/* hero */
.hero{top:56px;left:0;width:1200px;height:510px;overflow:hidden}
.hero-photo{inset:0;background:linear-gradient(180deg,#6e6f8e 0%,#c88a78 22%,#8a7d6a 40%,#3f6a4a 58%,#3e8fae 75%,#2b7db0 100%)}
.hero-wave{position:absolute;left:0;top:0}
.hero h1{position:absolute;top:188px;left:0;width:1200px;text-align:center;color:var(--white);font-size:31px;line-height:40px;font-weight:700;text-shadow:0 2px 6px rgba(0,0,0,.35)}

/* video */
.video-kicker{top:664px;left:0;width:1200px;text-align:center;color:var(--blue-text);font-size:12px}
.video-title{top:682px;left:0;width:1200px;text-align:center;color:var(--blue-text);font-size:23px;font-weight:700}
.blue-band{top:1058px;left:0;width:1200px;height:830px;background:var(--blue)}
.video-frame{top:734px;left:262px;width:676px;height:402px;background:var(--white);padding:7px;box-shadow:0 2px 10px rgba(0,0,0,.12)}
.video-photo{width:100%;height:100%;background:linear-gradient(180deg,#4a9ee0 0%,#9fd0f0 38%,#2cc3d3 55%,#19b7c9 100%)}
.play{position:absolute;left:302px;top:160px;width:72px;height:72px;border-radius:50%;background:#1d5fa6;border:4px solid rgba(255,255,255,.35)}

/* vouchers */
.give-title{top:1202px;left:0;width:1200px;text-align:center;color:var(--white);font-size:26px;line-height:34px;font-weight:700}
.give-sub{top:1272px;left:0;width:1200px;text-align:center;color:var(--white);font-size:13px}
.voucher{position:absolute;top:1344px;width:251px;height:153px;background:var(--white);display:flex}
.voucher-photo{width:123px;height:153px;background:linear-gradient(180deg,#b8302f 0%,#e9e4e0 30%,#d9d3cc 100%);border:3px solid #fff}
.voucher-info{padding:14px 0 0 14px;font-size:11px;line-height:17px}
.voucher-info .name{color:var(--blue-text);font-weight:700;font-size:12px}
.voucher-info .kind{color:var(--orange);margin-bottom:9px}
.voucher-info .note{color:var(--muted)}
.voucher-info .price{color:var(--blue-text);font-weight:700;font-size:12px}
.slider-track{top:1546px;left:383px;width:434px;height:1px;background:rgba(255,255,255,.3)}
.slider-thumb{top:1537px;left:591px;width:18px;height:18px;border-radius:4px;background:#cfe3f6}

.stay-frame{top:1701px;left:209px;width:782px;height:402px;background:var(--white);padding:7px;box-shadow:0 2px 10px rgba(0,0,0,.1)}
.stay-photo{width:100%;height:100%;background:linear-gradient(180deg,#dfe6ec 0%,#b9c7d2 38%,#6d5a48 52%,#2ea3b4 70%,#157c8e 100%)}
.pitch{top:2128px;left:240px;width:720px;text-align:center;font-size:17px;line-height:26px;color:var(--text)}
.pitch b{color:var(--blue-text);font-weight:700}

/* incentives */
.incentives{top:2330px;left:0;width:1200px;height:758px;background:var(--grey-bg)}
.incentives-title{top:2398px;left:0;width:1200px;text-align:center;color:var(--blue-text);font-size:27px;line-height:35px;font-weight:700}
.tile{position:absolute}
.tile-card{position:absolute;background:var(--white);box-shadow:0 2px 8px rgba(0,0,0,.08);display:flex;align-items:center;gap:12px;padding:0 22px;font-size:11px;font-weight:600;line-height:15px;color:#333}
.tile-card .ico{width:26px;height:26px;flex:none}
.tile-card small{display:block;font-weight:400;color:#555;margin-top:6px}

/* ad packs */
.adpacks{top:3088px;left:0;width:1200px;height:436px;background:var(--blue)}
.adpacks-title{top:3170px;left:156px;color:var(--white);font-size:27px;line-height:35px;font-weight:700}
.adpacks-copy{top:3255px;left:156px;width:290px;color:var(--white);font-size:15.5px;line-height:24px}
.ad-shadow{top:3157px;left:590px;width:374px;height:274px;background:#1e2a3a;border-radius:8px}
.ad-panel{top:3163px;left:512px;width:532px;height:262px;background:var(--white);border-radius:8px;padding:22px 20px;display:flex;gap:12px}
.ad-sample{flex:1;border:1px solid #e2e2e2}
.ad-dots{top:3444px;left:720px;display:flex;gap:6px}
.ad-dots i{width:9px;height:9px;border-radius:50%;border:1px solid rgba(255,255,255,.55)}
.ad-dots i.on{background:#cfe3f6}

/* testimonials */
.testi-title{top:3590px;left:0;width:1200px;text-align:center;color:var(--blue-text);font-size:25px;font-weight:700}
.quote-badge{top:3646px;left:565px;width:70px;height:70px;border-radius:50%;background:#444;border:4px solid #ddd;color:#fff;font-size:44px;line-height:86px;text-align:center;font-weight:700}
.testi-text{top:3740px;left:182px;width:836px;text-align:center;color:#6d6d6d;font-size:12.5px;line-height:21px}
.arrow{top:3797px}
.author-photo{top:3890px;left:538px;width:48px;height:48px;border-radius:50%;background:linear-gradient(180deg,#e7d4bd,#b79a7e);border:3px solid #dbe8f6}
.author{top:3898px;left:596px;font-size:13px;line-height:16px}
.author b{color:var(--blue-text);display:block}
.author span{color:var(--muted);font-size:10.5px}

/* footer */
.site-footer{top:4080px;left:0;width:1200px;height:30px;background:var(--blue-deep);color:var(--white);font-size:11px}
.site-footer .copy{position:absolute;left:156px;top:8px}
.site-footer .links{position:absolute;left:832px;top:8px;display:flex;gap:18px}
</style>
</head>
<body>

<header class="abs site-header">
  <div class="brand"><span class="brand-mark"></span>BrightLane Promo Works</div>
  <nav class="account-links">
    <span><svg width="11" height="11" viewBox="0 0 12 12" fill="none" stroke="currentColor" stroke-width="1.3"><circle cx="6" cy="6" r="5"/><path d="M4 6h4M6.5 4.5 8 6 6.5 7.5"/></svg>Login</span>
    <span><svg width="11" height="11" viewBox="0 0 12 12" fill="none" stroke="currentColor" stroke-width="1.3"><circle cx="6" cy="4" r="2.5"/><path d="M1.5 11.5c0-2.5 2-4 4.5-4s4.5 1.5 4.5 4"/></svg>Sign Up</span>
  </nav>
</header>

<section class="abs hero">
  <div class="photo hero-photo" role="img" aria-label="Tropical beach with limestone cliffs at sunset"></div>
  <svg class="hero-wave" width="1200" height="510" viewBox="0 0 1200 510">
    <path d="M0 510 L0 440 C250 540 500 515 700 500 C900 485 1080 400 1200 368 L1200 510 Z" fill="#ffffff"/>
    <path d="M0 362 C250 470 450 505 650 500 C850 492 1050 420 1200 365 L1200 368 C1080 400 900 485 700 500 C500 515 250 540 0 440 Z" fill="#1a72c2"/>
  </svg>
  <h1>Imagine Being Able To Offer BOGO<br>Deals With Every Booking!</h1>
  <a class="btn btn-orange" style="left:489px;top:283px;width:222px">Sign Up For 14 Days Risk Free</a>
</section>

<p class="abs video-kicker">Watch Below To See How Your Industry Uses Our Incentives To</p>
<h2 class="abs video-title">SKYROCKET THEIR SALES!</h2>

<div class="abs blue-band"></div>

<div class="abs video-frame">
  <div class="video-photo" role="img" aria-label="Thatched hut at the end of a pier over turquoise water"></div>
  <svg class="play" viewBox="0 0 72 72" width="72" height="72"><path d="M28 22 L50 34 L28 46 Z" fill="#fff"/></svg>
</div>

<h2 class="abs give-title">GIVE AWAY AN UNLIMITED AMOUNT OF<br>COMPLIMENTARY GIFT VOUCHERS REDEEMABLE FOR:</h2>
<p class="abs give-sub">(without having to personally fulfill or pay for any of them yourself!)</p>

<div class="voucher" style="left:156px">
  <div class="voucher-photo" role="img" aria-label="Hotel saving voucher card"></div>
  <div class="voucher-info"><div class="name">Hotel Saving</div><div class="kind">Cards</div><div class="note">Complimentary</div><div class="price">$100-$500</div><div class="note">Hotel Cards</div></div>
</div>
<div class="voucher" style="left:431px">
  <div class="voucher-photo" role="img" aria-label="Smart device voucher card"></div>
  <div class="voucher-info"><div class="name">Smart Device</div><div class="kind">Cards</div><div class="note">Complimentary</div><div class="price">Smart</div><div class="note">Devices</div></div>
</div>
<div class="voucher" style="left:707px">
  <div class="voucher-photo" role="img" aria-label="Restaurant dining voucher card"></div>
  <div class="voucher-info"><div class="name">Restaurant</div><div class="kind">Cards</div><div class="note">Complimentary</div><div class="price">$100-$500</div><div class="note">Dining Cards</div></div>
</div>
<div class="voucher" style="left:982px">
  <div class="voucher-photo" role="img" aria-label="Cruise getaway voucher card"></div>
  <div class="voucher-info"><div class="name">Cruise</div><div class="kind">Cards</div><div class="note">Cruise</div><div class="price">$100-$500</div><div class="note">Getaways</div></div>
</div>

<div class="abs slider-track"></div>
<div class="abs slider-thumb"></div>
<a class="btn btn-grey" style="left:487px;top:1593px;width:224px">Sign Up For 14 Days Risk Free</a>

<div class="abs stay-frame">
  <div class="stay-photo" role="img" aria-label="Overwater bungalows along a wooden walkway"></div>
</div>

<p class="abs pitch">Attract More New Customers Giving Away Free Vacation Certificates, <b>Cruise Vouchers, Smart Devices, Dining Takeout Vouchers</b> And More. You'll Never Pay For A Single Certificate, Vacation or Any Item, Ever.</p>
<a class="btn btn-orange" style="left:525px;top:2224px;width:150px">Book A Live Call</a>

<section class="abs incentives"></section>
<h2 class="abs incentives-title">OUR MARKETING INCENTIVES<br>CAN HELP YOU WITH</h2>

<div class="tile photo" style="left:156px;top:2497px;width:337px;height:435px;background:linear-gradient(180deg,#e9ecef,#c9ced4 60%,#8f98a3)" role="img" aria-label="Traveler with suitcase in an airport terminal"></div>
<div class="tile-card" style="left:185px;top:2853px;width:281px;height:112px;align-items:flex-start;padding-top:26px">
  <svg class="ico" viewBox="0 0 26 26" fill="#6aaee8"><rect x="3" y="9" width="20" height="5"/><rect x="5" y="14" width="16" height="10"/><rect x="12" y="9" width="2" height="15" fill="#fff"/></svg>
  <div>WELCOME GIFTS<small>Give Them As A Gift To<br>Welcome A Client Into Their<br>New Adventure.</small></div>
</div>

<div class="tile photo" style="left:519px;top:2497px;width:250px;height:189px;background:linear-gradient(180deg,#7fb4d8,#3c8a6a 55%,#3d9fb4)" role="img" aria-label="Wooden pier leading to a green island"></div>
<div class="tile-card" style="left:538px;top:2644px;width:212px;height:74px">
  <svg class="ico" viewBox="0 0 26 26" fill="#6aaee8"><path d="M4 10h5l9-5v16l-9-5H4z"/><rect x="7" y="16" width="3" height="6"/></svg>
  <div>SPECIAL PROMOTION<br>GIVEAWAY</div>
</div>

<div class="tile photo" style="left:793px;top:2497px;width:251px;height:189px;background:linear-gradient(180deg,#b7c3cf,#d69a6b 60%,#5f5048)" role="img" aria-label="Two friends on a swing at sunset"></div>
<div class="tile-card" style="left:812px;top:2644px;width:212px;height:74px">
  <svg class="ico" viewBox="0 0 26 26" fill="none" stroke="#6aaee8" stroke-width="2"><circle cx="8" cy="8" r="4"/><circle cx="18" cy="16" r="4"/><path d="M2 20c0-4 3-6 6-6M24 26"/></svg>
  <div>REFERRAL<br>GIFTS</div>
</div>

<div class="tile photo" style="left:519px;top:2743px;width:250px;height:189px;background:linear-gradient(180deg,#e0a8b8,#f0c3c6 50%,#c497b5)" role="img" aria-label="Airliner flying above pink clouds"></div>
<div class="tile-card" style="left:538px;top:2892px;width:212px;height:73px">
  <svg class="ico" viewBox="0 0 26 26" fill="#6aaee8"><path d="M2 14l9-2 7-9h3l-4 9 7 1-1 3-7-1-3 9h-3l1-9-8 1z"/></svg>
  <div>ENTICEMENT FOR<br>BOOKING A FLIGHT</div>
</div>

<div class="tile photo" style="left:793px;top:2743px;width:251px;height:189px;background:linear-gradient(180deg,#3f6e52,#dfe6ea 45%,#2d6f99)" role="img" aria-label="Cruise ship sailing past a green coastline"></div>
<div class="tile-card" style="left:812px;top:2892px;width:212px;height:73px">
  <svg class="ico" viewBox="0 0 26 26" fill="#6aaee8"><rect x="9" y="5" width="8" height="6"/><path d="M3 13h20l-3 8H6z"/></svg>
  <div>GIFTS FOR BOOKING<br>A CRUISE</div>
</div>

<a class="btn btn-grey" style="left:525px;top:2997px;width:150px">Book A Live Call</a>

<section class="abs adpacks"></section>
<h2 class="abs adpacks-title">PLUG-IN-PLAY<br>AD PACKS</h2>
<p class="abs adpacks-copy">Proven FeedSpace™ Ad Templates, High-Converting Banner Ad Templates To Use With The SearchGrid™ Display Network Plus Time-Tested Print Ad Templates That We Provide To You For Free With Your BrightLane Package.</p>
<div class="abs ad-shadow"></div>
<div class="abs ad-panel">
  <div class="ad-sample" style="background:linear-gradient(180deg,#fff 15%,#2a1a14 30%,#5a3a22 70%,#fff 85%)" role="img" aria-label="Social feed ad template for a free cruise offer"></div>
  <div class="ad-sample" style="background:linear-gradient(180deg,#fff 15%,#2a1a14 35%,#6a4426 75%,#fff 90%)" role="img" aria-label="Social post ad template for a free cruise offer"></div>
  <div class="ad-sample" style="background:linear-gradient(180deg,#fff 10%,#1a1a1a 15%,#4a3520 70%,#c8901c 95%)" role="img" aria-label="Web banner ad template for a free cruise offer"></div>
  <div class="ad-sample" style="background:linear-gradient(180deg,#fff 10%,#1a1a1a 15%,#3d2a1a 70%,#1a1a1a 95%)" role="img" aria-label="Print ad template for a free cruise offer"></div>
</div>
<div class="abs ad-dots"><i></i><i class="on"></i><i></i><i></i><i></i><i></i><i></i><i></i></div>

<h2 class="abs testi-title">TESTIMONIALS</h2>
<div class="abs quote-badge">“</div>
<p class="abs testi-text">I have been using BrightLane for 6 months and have been so impressed with this company. I have used the incentives with my customers to encourage repeat business and referrals. It has always been a pleasure to work with my consultant, Marcus. He calls me by name when we talk on the phone, and treats me like a professional and a friend. I have had several clients redeem their incentives, and all were incredibly pleased with them. Redemption is easy and fast. This strengthens my belief in BrightLane, and assures that I will use their services for a long time! I would reccomend BrightLane to all my business associates, and anyone who needs an incentive program to take their business to the next level.</p>
<svg class="abs arrow" style="left:122px" width="14" height="22" viewBox="0 0 14 22" fill="none" stroke="#9cc5ea" stroke-width="2"><path d="M11 2 2 11l9 9"/></svg>
<svg class="abs arrow" style="left:1063px" width="14" height="22" viewBox="0 0 14 22" fill="none" stroke="#1b6cbf" stroke-width="2"><path d="M3 2l9 9-9 9"/></svg>
<div class="abs author-photo" role="img" aria-label="Customer portrait"></div>
<div class="abs author"><b>Dana m.</b><span>Lorem Ipsum</span></div>
<a class="btn btn-orange" style="left:489px;top:3972px;width:222px">Sign Up For 14 Days Risk Free</a>

<footer class="abs site-footer">
  <div class="copy">Copyright © 2024 BrightLane, All rights reserved</div>
  <div class="links"><span>Privacy Policy</span><span>Term And Conditions</span></div>
</footer>

</body>
</html>
```